Verdano Harvest - Stationery Design Project

We need a stationary for our business. We grow roots and fruits in Central and South America, we import and distribute in FL, USA. We do fresh and frozen products.

Target Market(s)

Small and big supermarkets, wholesalers, traders, distributors, etc

Industry/Entity Type

Business

```html
<!DOCTYPE html>
<html lang="en">
<head>
<meta charset="utf-8">
<title>Verdano Harvest — Stationery</title>
<link href="https://fonts.googleapis.com/css2?family=Raleway:wght@300;400;500&display=swap" rel="stylesheet">
<style>
  :root {
    --ochre: #c2761c;
    --ochre-dark: #a9640f;
    --paper: #ffffff;
    --paper-edge: #dcdcdc;
    --backdrop: #ececec;
    --leaf: #4f6b2a;
    --ink: #6a6a6a;
    --rule: #b9b9b9;
  }
  * { box-sizing: border-box; margin: 0; padding: 0; }
  html, body { width: 1200px; height: 886px; overflow: hidden; }
  body {
    background: var(--backdrop);
    font-family: "Raleway", Arial, sans-serif;
    color: var(--ink);
    position: relative;
  }
  .piece {
    position: absolute;
    box-shadow: 0 2px 6px rgba(0,0,0,.12);
  }
  .piece--paper { background: var(--paper); }
  .piece--ochre { background: var(--ochre); }

  .wordmark {
    display: flex; align-items: center; gap: 6px;
    font-weight: 400; letter-spacing: .12em; text-transform: uppercase;
    white-space: nowrap;
  }
  .wordmark__dot { width: 7px; height: 7px; border-radius: 50%; background: var(--leaf); flex: none; }
  .wordmark--on-paper { color: var(--ochre); }
  .wordmark--on-ochre { color: #fff; }

  .fine { font-size: 6.5px; line-height: 1.6; letter-spacing: .04em; }
  .fine--light { color: rgba(255,255,255,.9); }
  .rule { height: 1px; background: var(--rule); }

  /* Letterhead */
  .letterhead { left: 40px; top: 50px; width: 300px; height: 424px; }
  .letterhead .wordmark { position: absolute; top: 34px; left: 0; right: 0; justify-content: center; font-size: 13px; }
  .letterhead__footer { position: absolute; left: 30px; right: 30px; bottom: 26px; text-align: right; }
  .letterhead__footer .rule { margin-bottom: 6px; }

  /* Folder */
  .folder { left: 370px; top: 50px; width: 300px; height: 424px; }
  .folder .wordmark { position: absolute; top: 60px; left: 0; right: 0; justify-content: center; font-size: 15px; }
  .folder__web { position: absolute; right: 22px; bottom: 20px; }

  /* Envelope */
  .envelope { left: 700px; top: 50px; width: 460px; height: 230px; overflow: hidden; }
  .envelope__flap { position: absolute; top: 0; left: 0; width: 460px; height: 80px; }
  .envelope__flap path { fill: var(--ochre); }

  /* Note sheet */
  .note { left: 700px; top: 310px; width: 460px; height: 220px; }
  .note .wordmark { position: absolute; top: 78px; left: 0; right: 0; justify-content: center; font-size: 15px; }
  .note__footer { position: absolute; left: 40px; right: 40px; bottom: 22px; text-align: right; }
  .note__footer .rule { margin-bottom: 6px; }

  /* Business cards */
  .card { width: 200px; height: 114px; }
  .card--front { left: 40px; top: 520px; }
  .card--front .wordmark { position: absolute; inset: 0; justify-content: center; font-size: 11px; }
  .card--back { left: 40px; top: 656px; }
  .card--back .wordmark { position: absolute; top: 16px; left: 0; right: 0; justify-content: center; font-size: 9px; }
  .card__person { position: absolute; top: 40px; left: 0; right: 0; text-align: center; }
  .card__name { font-size: 8px; font-weight: 500; color: var(--ochre); letter-spacing: .08em; text-transform: uppercase; }
  .card__role { font-size: 6.5px; letter-spacing: .06em; }
  .card__contact { position: absolute; bottom: 12px; left: 0; right: 0; text-align: center; }

  /* Notebook */
  .notebook { left: 300px; top: 520px; width: 240px; height: 330px; }
  .notebook__spiral { position: absolute; left: 6px; top: 12px; width: 10px; height: 306px; }
  .notebook__spiral circle { fill: var(--backdrop); stroke: #555; stroke-width: 1; }
  .notebook .wordmark { position: absolute; top: 70px; left: 16px; right: 0; justify-content: center; font-size: 13px; }
  .notebook__web { position: absolute; right: 18px; bottom: 16px; }

  /* Key tag & eraser */
  .keytag { left: 600px; top: 560px; width: 150px; height: 80px; border-radius: 6px; }
  .keytag .wordmark { position: absolute; inset: 0; justify-content: center; font-size: 8px; }
  .eraser { left: 600px; top: 680px; width: 150px; height: 60px; border-radius: 3px; }
  .eraser .wordmark { position: absolute; inset: 0; justify-content: center; font-size: 8px; }
</style>
</head>
<body>

  <section class="piece piece--paper letterhead" aria-label="Letterhead">
    <div class="wordmark wordmark--on-paper"><span class="wordmark__dot"></span>Verdano Harvest</div>
    <div class="letterhead__footer">
      <div class="rule"></div>
      <p class="fine">www.verdanoharvest.com</p>
      <p class="fine">Verdano Harvest LLC · 4120 Palm Grove Ave, Miami, FL 33142</p>
      <p class="fine">T +1 305 555 0148 · F +1 305 555 0149</p>
    </div>
  </section>

  <section class="piece piece--ochre folder" aria-label="Presentation folder">
    <div class="wordmark wordmark--on-ochre"><span class="wordmark__dot"></span>Verdano Harvest</div>
    <p class="fine fine--light folder__web">www.verdanoharvest.com</p>
  </section>

  <section class="piece piece--paper envelope" aria-label="Envelope">
    <svg class="envelope__flap" viewBox="0 0 460 80" aria-hidden="true">
      <path d="M0 0 H460 V40 Q460 60 440 62 L20 62 Q0 60 0 40 Z"/>
    </svg>
  </section>

  <section class="piece piece--paper note" aria-label="Compliment sheet">
    <div class="wordmark wordmark--on-paper"><span class="wordmark__dot"></span>Verdano Harvest</div>
    <div class="note__footer">
      <div class="rule"></div>
      <p class="fine">4120 Palm Grove Ave, Miami, FL 33142</p>
    </div>
  </section>

  <section class="piece piece--ochre card card--front" aria-label="Business card, front">
    <div class="wordmark wordmark--on-ochre"><span class="wordmark__dot"></span>Verdano Harvest</div>
  </section>

  <section class="piece piece--paper card card--back" aria-label="Business card, back">
    <div class="wordmark wordmark--on-paper"><span class="wordmark__dot"></span>Verdano Harvest</div>
    <div class="card__person">
      <p class="card__name">Mara Ellison</p>
      <p class="card__role">Sales Director</p>
    </div>
    <div class="card__contact">
      <p class="fine">4120 Palm Grove Ave, Miami, FL 33142</p>
      <p class="fine">T +1 305 555 0148 · info@verdanoharvest.com</p>
    </div>
  </section>

  <section class="piece piece--ochre notebook" aria-label="Spiral notebook cover">
    <svg class="notebook__spiral" viewBox="0 0 10 306" aria-hidden="true">
      <circle cx="5" cy="4" r="3"/><circle cx="5" cy="16" r="3"/><circle cx="5" cy="28" r="3"/><circle cx="5" cy="40" r="3"/>
      <circle cx="5" cy="52" r="3"/><circle cx="5" cy="64" r="3"/><circle cx="5" cy="76" r="3"/><circle cx="5" cy="88" r="3"/>
      <circle cx="5" cy="100" r="3"/><circle cx="5" cy="112" r="3"/><circle cx="5" cy="124" r="3"/><circle cx="5" cy="136" r="3"/>
      <circle cx="5" cy="148" r="3"/><circle cx="5" cy="160" r="3"/><circle cx="5" cy="172" r="3"/><circle cx="5" cy="184" r="3"/>
      <circle cx="5" cy="196" r="3"/><circle cx="5" cy="208" r="3"/><circle cx="5" cy="220" r="3"/><circle cx="5" cy="232" r="3"/>
      <circle cx="5" cy="244" r="3"/><circle cx="5" cy="256" r="3"/><circle cx="5" cy="268" r="3"/><circle cx="5" cy="280" r="3"/>
      <circle cx="5" cy="292" r="3"/><circle cx="5" cy="302" r="3"/>
    </svg>
    <div class="wordmark wordmark--on-ochre"><span class="wordmark__dot"></span>Verdano Harvest</div>
    <p class="fine fine--light notebook__web">www.verdanoharvest.com</p>
  </section>

  <section class="piece piece--paper keytag" aria-label="Key tag">
    <div class="wordmark wordmark--on-paper"><span class="wordmark__dot"></span>Verdano Harvest</div>
  </section>

  <section class="piece piece--ochre eraser" aria-label="Eraser">
    <div class="wordmark wordmark--on-ochre"><span class="wordmark__dot"></span>Verdano Harvest</div>
  </section>

</body>
</html>
```